Letterhead for Dorian Welk

I need a letterhead based on the business card design

Industry/Entity Type

Business

Requirements
Must have
• Footer: Dorian Welk Naturopath
Shop 4123c, 46 Carrow Lane, Sydney 2000

```html
<!DOCTYPE html>
<html lang="en">
<head>
<meta charset="utf-8">
<title>Dorian Welk Naturopath – Letterhead</title>
<link href="https://fonts.googleapis.com/css2?family=Montserrat:wght@400;700&display=swap" rel="stylesheet">
<style>
  :root {
    --orange: #f0921e;
    --orange-soft: #f6b25c;
    --leaf-pale: #fbe3c6;
    --white: #ffffff;
    --paper: #ffffff;
  }
  * { margin: 0; padding: 0; box-sizing: border-box; }
  html, body { width: 857px; height: 1200px; overflow: hidden; background: var(--paper); }
  body { font-family: "Montserrat", Arial, sans-serif; position: relative; }

  .letterhead { position: relative; width: 857px; height: 1200px; background: var(--paper); }

  .header-band {
    position: absolute; left: 0; top: 0; width: 857px; height: 232px;
    background: var(--orange); overflow: hidden;
  }
  .header-foliage {
    position: absolute; right: 0; top: 0; width: 330px; height: 232px;
    background: linear-gradient(120deg, rgba(255,255,255,0) 0%, rgba(255,255,255,0.18) 45%, rgba(255,255,255,0.08) 100%);
  }
  .brand-mark {
    position: absolute; left: 92px; top: 30px; width: 110px; height: 110px;
    border-radius: 50%; background: var(--orange-soft);
  }
  .brand {
    position: absolute; left: 230px; width: 520px; top: 84px; text-align: center; color: var(--white);
  }
  .brand-name { font-weight: 700; font-size: 42px; letter-spacing: 2px; line-height: 1; }
  .brand-rule { height: 2px; background: var(--white); margin: 20px 0 8px; }
  .brand-tagline { font-size: 15px; letter-spacing: 7px; }
  .brand-address { font-size: 11px; margin-top: 16px; }

  .side-foliage {
    position: absolute; right: 0; top: 370px; width: 440px; height: 780px;
    background: radial-gradient(ellipse at 70% 45%, var(--leaf-pale) 0%, rgba(251,227,198,0.6) 45%, rgba(255,255,255,0) 75%);
  }

  .footer-contact {
    position: absolute; left: 0; right: 0; top: 1135px; text-align: center;
    font-size: 12px; color: var(--orange);
  }
  .footer-contact span + span { margin-left: 10px; }

  .edge-accent {
    position: absolute; left: 0; top: 1088px; width: 8px; height: 112px; background: var(--orange);
  }
</style>
</head>
<body>
  <div class="letterhead">
    <header class="header-band">
      <div class="header-foliage" role="img" aria-label="Faint leaf decoration"></div>
      <div class="brand-mark"></div>
      <div class="brand">
        <div class="brand-name">DORIAN WELK</div>
        <div class="brand-rule"></div>
        <div class="brand-tagline">NATUROPATHY</div>
        <div class="brand-address">Shop 4123c, 46 Carrow Lane, Sydney 2000</div>
      </div>
    </header>

    <div class="side-foliage" role="img" aria-label="Large faint leaf decoration"></div>

    <footer class="footer-contact">
      <span>dorianwelk.com.au</span><span>hello@dorianwelk.com.au</span>
    </footer>
    <div class="edge-accent"></div>
  </div>
</body>
</html>
```